Brindlefax Brochure

I require a brochure for my business called Brindlefax Services or "Brindlefax" for short. We obtain subpoena material on behalf of lawfirms in Sydney and focus purely on the sydney-city based locations.

www.brindlefax-demo.com.au

My website is quite comprehensive and has all the information you may require.

The design should stand out as to price and trust to know we would complete the job professionally remember that my clients are law firms. I have a few documents that i will attach that will show you what i am looking for. I will leave colour upto the designer.

I require ongoing work including logos, other brochures so this will be an ongoing contract. I require someone who will communicate with me and is available for a range of projects.

Target Market(s)

Law firms

Industry/Entity Type

Business

Colors

Designer to choose colors to be used in the design.

Requirements
Must have
• professional and instill trust and security
Nice to have
• this market is dominated by 3 other firms we are a new firm looking to establish and take a number of their clients who are paying through the nose.

```html
<!DOCTYPE html>
<html lang="en">
<head>
<meta charset="utf-8">
<title>Brindlefax Services – Trifold Brochure</title>
<link rel="stylesheet" href="https://fonts.googleapis.com/css2?family=Arimo:ital,wght@0,400;0,700;1,400;1,700&family=Roboto+Condensed:wght@400;700&display=swap">
<style>
:root{
  --red:#d0121b;
  --red-deep:#8e0f14;
  --maroon:#6e0c10;
  --charcoal:#24262c;
  --ink:#16171b;
  --white:#ffffff;
  --paper:#f4f4f4;
  --text:#333338;
  --muted:#bfc1c6;
  --backdrop:#e7e4df;
}
*{box-sizing:border-box;margin:0;padding:0}
html,body{width:1200px;height:1080px;overflow:hidden;background:var(--backdrop)}
body{position:relative;font-family:"Arimo",Arial,sans-serif;color:var(--text)}

.spread{position:absolute;left:240px;width:720px;height:510px;display:flex;box-shadow:0 6px 18px rgba(0,0,0,.25);background:var(--white)}
.spread--outside{top:18px}
.spread--inside{top:552px}
.panel{position:relative;width:240px;height:510px;overflow:hidden}
.panel + .panel{border-left:1px solid rgba(0,0,0,.08)}

.photo{position:absolute;left:0;right:0}
.wave{position:absolute;left:0;width:240px}

.tab{display:inline-block;background:var(--red);color:var(--white);font-weight:700;font-size:11px;padding:4px 10px 4px 14px;border-radius:0 3px 3px 0}
.tab--italic{font-style:italic}
.copy{font-size:7px;line-height:1.4}

/* outside: pricing flap */
.pricing__tab{position:absolute;top:16px;left:0}
.pricing__text{position:absolute;top:44px;left:18px;right:18px;font-style:italic}
.pricing__offer{position:absolute;top:104px;left:18px;width:150px;height:66px;background:var(--red-deep);border:2px solid var(--white);outline:1px solid var(--red-deep);border-radius:8px;color:var(--white);font-style:italic;padding:5px 10px}
.pricing__offer-lead{font-size:10px;font-weight:700}
.pricing__offer-figure{font-size:30px;font-weight:700;line-height:1}
.pricing__offer-tail{font-size:9px;font-weight:700;text-align:right;margin-top:-8px}

/* outside: contact */
.contact{position:absolute;top:300px;left:22px;right:14px;list-style:none;color:var(--white)}
.contact li{display:flex;align-items:flex-start;gap:8px;font-size:8px;line-height:1.3;margin-bottom:8px}
.contact .icon{flex:none;width:14px;height:14px;border-radius:3px;background:var(--red);display:flex;align-items:center;justify-content:center}

/* cover */
.brand{position:absolute;top:26px;left:22px;right:10px;text-align:center}
.brand__name{font-family:"Roboto Condensed",Arial,sans-serif;font-weight:700;color:var(--red);font-size:36px;line-height:1;letter-spacing:.5px}
.brand__sub{font-family:"Roboto Condensed",Arial,sans-serif;font-weight:400;color:var(--ink);font-size:16px;margin-top:2px}
.seal{position:absolute;z-index:5;width:70px;height:70px;border-radius:50%;background:var(--red);border:3px solid var(--ink);box-shadow:0 0 0 2px var(--white),0 0 0 4px var(--ink);color:var(--white);text-align:center;font-weight:700;font-style:italic;display:flex;flex-direction:column;justify-content:center;line-height:1}
.seal__word{font-size:12px;font-weight:400}
.seal__figure{font-size:22px}
.cover__lower{position:absolute;left:0;right:0;bottom:0;height:170px;color:var(--white);padding:30px 14px 0 16px}
.cover__kicker{font-size:8px;text-align:right}
.cover__headline{font-size:14px;font-weight:700;text-align:right;line-height:1.1}
.cover__headline strong{font-size:21px}
.cover__note{color:var(--red);font-size:8.5px;text-align:right;margin-top:2px}
.venues{display:grid;grid-template-columns:1.3fr 1fr;gap:2px 8px;list-style:none;font-size:7px;margin-top:8px}
.venues li{display:flex;gap:4px}
.venues li::before{content:"";flex:none;width:5px;height:5px;margin-top:1.5px;background:var(--red)}
.cover__web{font-size:8px;color:var(--muted);text-align:center;margin-top:12px;border-top:1px solid #44474f;padding-top:4px}

/* inside */
.intro{position:absolute;top:206px;left:0;right:14px}
.intro .copy{padding:4px 0 0 16px}
.services-tab{margin-top:10px}
.service-list{list-style:none;padding-left:16px;margin-top:3px;font-size:7.5px}
.service-list li{display:flex;gap:4px;line-height:1.4}
.service-list li::before{content:"";width:5px;height:5px;margin-top:3px;background:var(--red)}
.ribbon{position:absolute;left:16px;top:462px;width:370px;height:24px;background:var(--red);color:var(--white);font-weight:700;font-size:11px;display:flex;align-items:center;justify-content:center;letter-spacing:.3px;white-space:nowrap;z-index:6;box-shadow:0 2px 4px rgba(0,0,0,.3)}

.block{position:absolute;left:0;right:0;top:150px;bottom:0;color:var(--white)}
.block__brand{padding:22px 10px 0 14px}
.block__brand .brand__name{color:var(--white);font-size:30px}
.block__brand .brand__sub{color:var(--white);font-size:14px}
.block__section{padding:8px 12px 0 14px}
.label{display:inline-block;background:var(--white);color:var(--red-deep);font-weight:700;font-size:10px;padding:2px 8px;border-radius:2px;margin-bottom:4px}

.ask{position:absolute;top:22px;left:16px;right:10px;color:var(--red);font-weight:700;font-size:15px;line-height:1.15}
.faq{position:absolute;top:222px;left:0;right:10px}
.faq__head{display:block;background:var(--red-deep);color:var(--white);font-weight:700;font-size:10px;padding:3px 10px 3px 16px;border-radius:0 3px 3px 0;margin-bottom:4px}
.faq .copy{padding:0 0 8px 16px}
</style>
</head>
<body>

<section class="spread spread--outside" aria-label="Brochure outside">

  <article class="panel panel--pricing">
    <h3 class="tab tab--italic pricing__tab">Photocopying Pricing</h3>
    <p class="copy pricing__text">With our new systems and process we have developed a unique way of reducing our costs and can save you more than 35% over our competitors. Contact us for a quote today! Simply provide your instructions via email to us directly.</p>
    <div class="pricing__offer">
      <div class="pricing__offer-lead">Save time and up to</div>
      <div class="pricing__offer-figure">30%</div>
      <div class="pricing__offer-tail">of costs</div>
    </div>
    <div class="photo" style="top:200px;bottom:0;background:linear-gradient(160deg,#d9dadc 0%,#9fa2a7 45%,#4a4c52 100%)" role="img" aria-label="Photo of an office photocopier in use"></div>
    <svg class="wave" style="top:170px" height="90" viewBox="0 0 240 90" aria-hidden="true">
      <path d="M0 0 H240 V30 C170 10 80 60 0 40 Z" fill="#fff"/>
      <path d="M0 22 C80 44 160 0 240 20 V34 C160 16 80 62 0 40 Z" fill="var(--red)"/>
      <path d="M0 44 C80 66 160 20 240 36 V42 C160 28 80 72 0 52 Z" fill="var(--red-deep)"/>
    </svg>
  </article>

  <article class="panel panel--contact" style="background:var(--charcoal)">
    <div class="photo" style="top:0;height:260px;background:linear-gradient(170deg,#6b3a1f 0%,#a0652e 45%,#3a2010 100%)" role="img" aria-label="Photo of scales of justice in a courtroom"></div>
    <svg class="wave" style="top:200px" height="90" viewBox="0 0 240 90" aria-hidden="true">
      <path d="M0 30 C80 60 160 10 240 40 V90 H0 Z" fill="var(--charcoal)"/>
      <path d="M0 22 C80 52 160 2 240 30 V40 C160 12 80 62 0 32 Z" fill="var(--red)"/>
      <path d="M0 14 C80 44 160 -6 240 22 V28 C160 2 80 52 0 22 Z" fill="#fff"/>
    </svg>
    <ul class="contact">
      <li><span class="icon"><svg width="9" height="9" viewBox="0 0 10 10"><path d="M5 0a3.5 3.5 0 0 0-3.5 3.5C1.5 6 5 10 5 10s3.5-4 3.5-6.5A3.5 3.5 0 0 0 5 0z" fill="#fff"/><circle cx="5" cy="3.5" r="1.2" fill="var(--red)"/></svg></span><span>48 Harbourline Street,<br>Sydney NSW 2000</span></li>
      <li><span class="icon"><svg width="9" height="9" viewBox="0 0 10 10"><path d="M2 0.5l2 2-1 1.3c.6 1.3 1.6 2.3 2.9 2.9L7.2 5.7l2 2-1.4 1.8C4.2 9.2 .8 5.8.3 2.1z" fill="#fff"/></svg></span><span>02-5550-0142</span></li>
      <li><span class="icon"><svg width="9" height="9" viewBox="0 0 10 10"><rect x="2.5" y="0.5" width="5" height="3" fill="#fff"/><rect x="0.5" y="3.5" width="9" height="4" rx="1" fill="#fff"/><rect x="2.5" y="6.5" width="5" height="3" fill="#fff" stroke="var(--red)" stroke-width=".6"/></svg></span><span>02-5550-0187</span></li>
      <li><span class="icon"><svg width="9" height="9" viewBox="0 0 10 10"><rect x="0.5" y="2" width="9" height="6" fill="#fff"/><path d="M0.5 2l4.5 3.5L9.5 2" fill="none" stroke="var(--red)" stroke-width=".8"/></svg></span><span>info@brindlefax-demo.com.au</span></li>
      <li><span class="icon"><svg width="9" height="9" viewBox="0 0 10 10"><circle cx="5" cy="5" r="4.2" fill="none" stroke="#fff"/><path d="M0.8 5h8.4M5 .8c-2.2 2.5-2.2 5.9 0 8.4M5 .8c2.2 2.5 2.2 5.9 0 8.4" fill="none" stroke="#fff" stroke-width=".7"/></svg></span><span>www.brindlefax-demo.com.au</span></li>
    </ul>
  </article>

  <article class="panel panel--cover" style="background:var(--white)">
    <div class="brand">
      <div class="brand__name">BRINDLEFAX</div>
      <div class="brand__sub">SERVICES PTY LTD</div>
    </div>
    <div class="photo" style="top:120px;height:230px;background:linear-gradient(180deg,#e9ecef 0%,#b8bec6 40%,#3b3f48 100%)" role="img" aria-label="Photo of a smiling businessman holding a folder in an office with colleagues"></div>
    <svg class="wave" style="top:96px" height="40" viewBox="0 0 240 40" aria-hidden="true">
      <path d="M0 0 H240 V18 C160 34 80 34 0 16 Z" fill="#fff"/>
      <path d="M0 12 C80 30 160 30 240 12 V20 C160 38 80 38 0 20 Z" fill="var(--red)"/>
    </svg>
    <svg class="wave" style="top:300px" height="60" viewBox="0 0 240 60" aria-hidden="true">
      <path d="M0 40 C80 46 170 30 240 4 V60 H0 Z" fill="var(--charcoal)"/>
      <path d="M0 34 C80 40 170 24 240 0 V6 C170 30 80 46 0 40 Z" fill="var(--red)"/>
    </svg>
    <div class="cover__lower" style="background:var(--charcoal)">
      <p class="cover__kicker">Need important legal documents</p>
      <h1 class="cover__headline">Delivered <strong>URGENTLY?</strong></h1>
      <p class="cover__note">Onsite copying and Uplifting of documents<br>and Court records at:</p>
      <ul class="venues">
        <li>Local Courts – Civic Court Centre</li>
        <li>NSW Supreme Court</li>
        <li>Sydney and Elizabeth Court Tower</li>
        <li>Family Court</li>
        <li>District Courts</li>
      </ul>
      <p class="cover__web">www.brindlefax-demo.com.au</p>
    </div>
    <div class="seal" style="top:262px;left:152px"><span class="seal__word">Save</span><span class="seal__figure">30%</span></div>
  </article>
</section>

<section class="spread spread--inside" aria-label="Brochure inside">

  <article class="panel panel--intro" style="background:var(--white)">
    <div class="photo" style="top:0;height:190px;background:linear-gradient(160deg,#f1f2f4 0%,#c9ccd2 55%,#8d9098 100%)" role="img" aria-label="Photo of a legal team meeting around a laptop"></div>
    <svg class="wave" style="top:160px" height="40" viewBox="0 0 240 40" aria-hidden="true">
      <path d="M0 20 C90 40 170 20 240 0 V40 H0 Z" fill="#fff"/>
      <path d="M0 12 C90 32 170 12 240 -8 V2 C170 22 90 40 0 20 Z" fill="var(--red)"/>
    </svg>
    <div class="intro">
      <h2 class="tab">Introduction</h2>
      <p class="copy">Brindlefax is a rapidly growing provider of secure and confidential document reproduction services. We assist prominent legal firms in Australia, corporate and government organisations and even sole practitioners. With years of experience, we understand what all our clients need and as a result we are committed to providing affordable quality processes and ensuring that all work is completed on time, every time.</p>
      <h2 class="tab services-tab">Our Services</h2>
      <p class="copy">We specialise in legal copying for the NSW District Court, Supreme Court &amp; Family Court.</p>
      <ul class="service-list">
        <li>Subpoena services</li>
        <li>File copying</li>
      </ul>
    </div>
  </article>

  <article class="panel panel--services" style="background:var(--white)">
    <div class="photo" style="top:0;height:190px;background:linear-gradient(200deg,#f4f5f6 0%,#cfd2d6 50%,#7f838b 100%)" role="img" aria-label="Photo of colleagues reviewing documents in a bright office"></div>
    <div class="block" style="background:linear-gradient(180deg,var(--red-deep),var(--maroon))">
      <svg class="wave" style="top:-30px" height="40" viewBox="0 0 240 40" aria-hidden="true">
        <path d="M0 30 C90 20 170 10 240 0 V40 H0 Z" fill="var(--red-deep)"/>
      </svg>
      <div class="block__brand">
        <div class="brand__name">BRINDLEFAX</div>
        <div class="brand__sub">SERVICES PTY LTD</div>
      </div>
      <div class="block__section">
        <h2 class="label">Subpoena Services</h2>
        <p class="copy">We can collect, copy AND deliver subpoenaed documents from each of Sydney's NSW District Court, Supreme Court &amp; Family Court. Then we can provide these documents in physical or even searchable PDF forms if required and deliver via DX or even hand deliver.</p>
      </div>
      <div class="block__section">
        <h2 class="label">File Copying Services</h2>
        <p class="copy">We can provide an electronic copy in PDF Searchable format if required. A hard copy is sent via dx or post on the same day if required.</p>
      </div>
    </div>
  </article>

  <article class="panel panel--urgent" style="background:var(--white)">
    <div class="photo" style="top:0;height:220px;background:var(--charcoal)"></div>
    <svg class="wave" style="top:170px" height="60" viewBox="0 0 240 60" aria-hidden="true">
      <path d="M0 50 C80 30 160 10 240 30 V0 H0 Z" fill="var(--charcoal)"/>
      <path d="M0 44 C80 24 160 4 240 24 V34 C160 14 80 34 0 54 Z" fill="var(--red-deep)"/>
    </svg>
    <p class="ask">Ask our friendly staff<br>for our pricing</p>
    <div class="seal" style="top:84px;left:86px"><span class="seal__word">Save</span><span class="seal__figure">30%</span></div>
    <div class="faq">
      <h2 class="faq__head">Need your Documents Urgently?</h2>
      <p class="copy">Whilst we normally deliver documents overnight via courier, express mail or DX to our clients, we also include a scan and email service for urgent access to your legal documents.</p>
      <p class="copy">This is extremely effective for our out-of-town clients who need to access their legal documents on the same day.</p>
      <h2 class="faq__head">Not a Client of Brindlefax?</h2>
      <p class="copy">Most of our clients have accounts with us and are invoiced on 30 day terms. If you expect to use Brindlefax regularly, feel free to open an account with us. An account will allow you to constantly check on the status of your task on our website.</p>
      <p class="copy">We also complete one-off requests and would be delighted to assist you even if you have not created an account with us. We accept various payment methods.</p>
    </div>
  </article>

  <div class="ribbon">FAST, ACCURATE AND AFFORDABLE COPYING</div>
</section>

</body>
</html>
```